Kindle Thread Pty Ltd Brochure and New Image Design

Initally we will be needing a A4 Folder design created as well as a Template for a Double Sided Flyer. We need a cutting edge design which we can incorporate into a Brochure, Flyer Handout, Website etc. Basically we are re-branding our company starting with an "About Us" Folder which we will be distributing to potential customers.
We are an Embroidery company that caters for mid-large companies dealing with clothing ranging from Corporate Attire to Workwear. Our current website has more information on what we do and you can use that as a valid reference point (www.kindlethread.com.au), However the website will be step 2 in freshening up our image.
Our company has been thriving over the 20 years we have been in business by supplying a higher quality product as well as Service that is second to none, unfortunately our branding image has been overlooked while we have spent more time/effort on our customer service.
We have used the colours Maroon (PMS 216C) Silver Grey (PMS Cool Gray 7) White and Black. We would like to maintain these colours but incorporate them together in a way that has a more "modern edgey" look.
Target Market(s)
Purchasing / Marketing Officers of Mid-Large Corporate Companies.
Industry/Entity Type
Clothing
Look and feel

```html
<!DOCTYPE html>
<html lang="en">
<head>
<meta charset="utf-8">
<title>Kindle Thread Pty Ltd — Folder Cover</title>
<link rel="stylesheet" href="https://fonts.googleapis.com/css2?family=Montserrat:wght@400;600&display=swap">
<style>
  :root {
    --maroon: #5e1f3b;
    --maroon-veil: rgba(110, 34, 68, 0.55);
    --silver: #dcdcdc;
    --photo-light: #c4c4c6;
    --photo-mid: #9d9aa2;
    --photo-dark: #2d3148;
    --page: #ffffff;
  }
  * { margin: 0; padding: 0; box-sizing: border-box; }
  html, body {
    width: 1200px;
    height: 849px;
    overflow: hidden;
    background: var(--page);
    font-family: "Montserrat", sans-serif;
  }
  .folder-spread {
    position: relative;
    width: 1200px;
    height: 849px;
    display: flex;
  }
  .folder-back {
    position: relative;
    width: 600px;
    height: 849px;
    background: var(--maroon);
  }
  .folder-back__swoosh {
    position: absolute;
    inset: 0;
    width: 600px;
    height: 849px;
  }
  .folder-front {
    position: relative;
    width: 600px;
    height: 849px;
    border-left: 1px solid var(--page);
    overflow: hidden;
  }
  .folder-front__photo {
    position: absolute;
    inset: 0;
    background:
      radial-gradient(ellipse 42% 60% at 62% 62%, var(--photo-dark) 0%, var(--photo-dark) 55%, transparent 75%),
      linear-gradient(180deg, var(--photo-light) 0%, var(--photo-mid) 100%);
  }
  .folder-front__band {
    position: absolute;
    left: 0;
    right: 0;
    top: 216px;
    height: 406px;
    background: var(--maroon-veil);
  }
</style>
</head>
<body>
  <main class="folder-spread">
    <section class="folder-back">
      <svg class="folder-back__swoosh" viewBox="0 0 600 849" aria-hidden="true">
        <path d="M4 849 L114 514 C150 590 215 624 330 626 L600 624 L600 849 Z" fill="var(--silver)"/>
      </svg>
    </section>
    <section class="folder-front">
      <div class="folder-front__photo" role="img" aria-label="Photograph of a businesswoman in a navy tailored suit jacket and pale pink shirt against a grey studio backdrop"></div>
      <div class="folder-front__band"></div>
    </section>
  </main>
</body>
</html>
```